Solvane Official Investment Guide 2015

60 Second Animated Presentation to be showcased at a large Mining Convention. Presentation promotes the launch of VEXTAL 2015, the Official Mining Investment Guide for the Convention. Also promotes HQT, the publisher. Presentation will be displayed in large screens on the exhibition floor, so it needs to be simple yet eye-catching and engaging. The cover of VEXTAL is on definition phase, but it has been mostly completed - please follow those colors + the blue from HQT logo.
Target Market(s)
Mining Professionals in Latin America
Industry/Entity Type
Mining
Requirements
Must have
- Animation as per Youtube link included on the brief
- Strong Illustrations
Nice to have
- Music as per youtube link included on the brief

```html
<!DOCTYPE html>
<html lang="es">
<head>
<meta charset="UTF-8">
<title>VEXTAL 2015 — HQT</title>
<link href="https://fonts.googleapis.com/css2?family=Bebas+Neue&family=Montserrat:wght@700;800&display=swap" rel="stylesheet">
<style>
  :root {
    --bg: #1f2e33;
    --white: #f2f2f2;
    --orange: #e0640a;
    --peach: #f2b07f;
  }
  html, body {
    margin: 0;
    padding: 0;
    width: 1200px;
    height: 674px;
    overflow: hidden;
    background: var(--bg);
  }
  .frame {
    position: relative;
    width: 1200px;
    height: 674px;
    overflow: hidden;
    background: var(--bg);
  }
  .kinetic-word {
    position: absolute;
    margin: 0;
    font-family: "Montserrat", Arial, sans-serif;
    font-weight: 800;
    line-height: 1;
    white-space: nowrap;
  }
  .kinetic-word--top {
    left: -8px;
    top: -68px;
    font-size: 168px;
    color: var(--white);
    letter-spacing: -2px;
  }
  .kinetic-word--bottom {
    left: 690px;
    top: 505px;
    font-size: 300px;
    color: var(--orange);
    letter-spacing: -6px;
  }
  .publisher {
    position: absolute;
    left: 185px;
    top: 240px;
    width: 300px;
    text-align: center;
    margin: 0;
    font-family: "Bebas Neue", Impact, sans-serif;
    font-size: 120px;
    line-height: 1;
    color: var(--white);
    letter-spacing: 4px;
  }
  .tagline {
    position: absolute;
    left: 603px;
    top: 0;
    margin: 0;
    font-family: "Bebas Neue", Impact, sans-serif;
    font-weight: 400;
  }
  .tagline span {
    position: absolute;
    left: 0;
    line-height: 1;
    white-space: nowrap;
  }
  .tagline .small { color: var(--peach); font-size: 43px; letter-spacing: 3px; }
  .tagline .big { color: var(--orange); }
  .line-es-su { top: 137px; }
  .line-fuente { top: 186px; font-size: 116px; letter-spacing: 5px; }
  .line-de { top: 302px; }
  .line-informacion { top: 352px; font-size: 88px; letter-spacing: 2px; }
  .line-referencia { top: 446px; }
  .line-referencia .de-small { font-size: 36px; letter-spacing: 2px; margin-right: 10px; }
  .line-referencia .ref { font-size: 63px; letter-spacing: 4px; }
</style>
</head>
<body>
<main class="frame">
  <p class="kinetic-word kinetic-word--top">cion es</p>

  <p class="publisher">HQT</p>

  <h1 class="tagline">
    <span class="small line-es-su">ES SU</span>
    <span class="big line-fuente">FUENTE</span>
    <span class="small line-de">DE</span>
    <span class="big line-informacion">INFORMACION</span>
    <span class="small line-referencia"><span class="de-small" style="position:static">DE</span><span class="ref" style="position:static">REFERENCIA</span></span>
  </h1>

  <p class="kinetic-word kinetic-word--bottom">RO</p>
</main>
</body>
</html>
```